Pinecrest 71 Studios needs a web design

We need a website design for a California based visual effects (VFX) company to show potential clients and employees who we are and what we do. We are currently focusing on compositing based tasks such as but not limited to multi-pass composites, green screen extraction, rotoscope, paint fixes and retimes. We like imagery that makes people think of 'California' such as the state flag, sunshine and the beach. The website should send a message that although we are a new company, we are not new to the vfx industry. The website needs to be compatible with mobile devices. We also need the ability to edit and modify the site.

Target Market(s)

Studio executive, producers and potential employees.

Industry/Entity Type

Flag

Coding

Coded - Design and coding required

Number of Pages Required

4 page

Font styles to use
Serif
Sans Serif

Requirements
Must have
• Must have space for company and individual biographies. Must have a page for a credits list and show reel. Must also have space for contact info ex. maps, email, social media.

```html
<!DOCTYPE html>
<html lang="en">
<head>
<meta charset="utf-8">
<title>Pinecrest 71 Studios — Visual Effects</title>
<link rel="stylesheet" href="https://fonts.googleapis.com/css2?family=Montserrat:wght@400;600;700&family=Noticia+Text:wght@400;700&display=swap">
<style>
:root{
  --page:#f3f3f3;
  --white:#ffffff;
  --ink:#1d1d1d;
  --muted:#555555;
  --teal-deep:#0a4f60;
  --teal:#0f7086;
  --teal-light:#3a97a8;
  --panel-dark:#2b2b2b;
  --panel-mid:#3a3a3a;
  --red:#d2322d;
  --orange:#e47a22;
  --link:#2b6cb5;
  --map-deep:#3c4a55;
  --map-light:#5d6b74;
  --sans:"Montserrat", Arial, sans-serif;
  --serif:"Noticia Text", Georgia, serif;
}
*{box-sizing:border-box;margin:0;padding:0}
html,body{width:1200px;height:2778px;overflow:hidden}
body{background:var(--page);color:var(--ink);font-family:var(--serif);position:relative}
.site{position:absolute;left:100px;top:0;width:1011px;height:2645px;background:var(--white)}

/* hero */
.hero{position:absolute;left:0;top:0;width:1011px;height:522px;overflow:hidden}
.hero__photo{position:absolute;inset:0;background:linear-gradient(180deg,var(--teal) 0%,var(--teal-light) 45%,var(--teal-deep) 100%)}
.brand{position:absolute;left:58px;top:38px;display:flex;align-items:center;gap:12px;font-family:var(--sans);font-weight:700;font-size:17px;color:var(--white)}
.brand__dot{width:16px;height:16px;border-radius:50%;background:var(--white)}
.nav{position:absolute;right:64px;top:52px;display:flex;gap:30px;font-family:var(--sans);font-size:15px;color:var(--white)}
.nav__item--active{border-bottom:3px solid var(--red);padding-bottom:4px}
.hero__title{position:absolute;left:0;width:100%;top:150px;text-align:center;font-family:var(--sans);font-weight:700;font-size:48px;line-height:56px;color:var(--white)}
.hero__lede{position:absolute;left:70px;width:871px;top:276px;text-align:center;font-size:17px;line-height:25px;color:var(--white)}
.hero__more{position:absolute;left:0;width:100%;top:428px;text-align:center;font-family:var(--sans);font-weight:600;font-size:14px;color:var(--white)}
.hero__arrow{position:absolute;left:490px;top:458px}

/* bio */
.bio{position:absolute;left:0;top:522px;width:1011px;height:389px}
.bio__photo{position:absolute;top:0;height:389px;width:505px}
.bio__photo--left{left:0;background:linear-gradient(160deg,var(--panel-mid),var(--panel-dark))}
.bio__photo--right{left:506px;background:linear-gradient(200deg,#4a4a4a,#262626)}
.bio__name{position:absolute;left:28px;top:28px;font-family:var(--sans);font-weight:700;font-size:19px;color:var(--white)}
.bio__intro{position:absolute;left:28px;top:58px;width:430px;font-family:var(--sans);font-size:14px;line-height:21px;color:var(--white)}
.bio__cta{position:absolute;left:28px;bottom:18px;font-family:var(--sans);font-weight:600;font-size:13px;color:var(--red)}
.bio__hint{position:absolute;left:534px;bottom:18px;font-family:var(--sans);font-weight:600;font-size:13px;color:#7a7a7a}

.about-card{position:absolute;left:0;top:925px;width:506px;height:264px;background:var(--white);border:1px solid #e2e2e2;padding:14px 28px}
.about-card__title{font-family:var(--sans);font-weight:700;font-size:13px;margin-bottom:6px}
.about-card__text{font-size:12.3px;line-height:20px;color:#333}

/* services */
.section-title{position:absolute;left:0;width:100%;text-align:center;font-family:var(--sans);font-weight:700;font-size:50px;color:var(--ink)}
.services__title{top:1228px}
.service{position:absolute;left:95px;display:flex;gap:22px;width:440px}
.service__icon{width:58px;height:58px;border-radius:50%;background:#fbeee2;flex:none;display:flex;align-items:center;justify-content:center}
.service__name{font-size:23px;line-height:26px}
.service__text{font-family:var(--sans);font-size:14px;line-height:17px;color:#333}
.services__lead{position:absolute;left:517px;top:1330px;width:450px;font-family:var(--sans);font-weight:700;font-size:23px;line-height:30px}
.services__photo{position:absolute;left:517px;top:1464px;width:425px;height:278px;background:linear-gradient(160deg,#8fb2cf 0%,#c7d6e2 45%,#5d6b77 100%)}

/* about */
.about__title{top:1790px}
.about__text{position:absolute;left:90px;width:831px;top:1862px;text-align:center;font-size:18.4px;line-height:26.5px;color:#222}
.about__brand{color:var(--link)}
.about__accent{color:var(--red)}

/* map */
.location{position:absolute;left:0;top:2139px;width:1011px;height:431px;background:linear-gradient(135deg,var(--map-light),var(--map-deep) 60%,#34404a)}
.location__text{position:absolute;left:67px;top:56px;width:380px;font-size:23px;line-height:29px;color:var(--white)}

/* footer */
.footer{position:absolute;left:0;top:2570px;width:1011px;height:75px;display:flex;align-items:center;justify-content:space-between;padding:0 67px}
.social{display:flex;gap:8px}
.social__item{width:17px;height:17px;background:#3b6aa6;border-radius:2px}
.social__item--red{background:#c94133}
.footer__legal{font-family:var(--sans);font-size:11px;color:#333}
.footer__legal b{color:var(--link);font-weight:600}
</style>
</head>
<body>
<div class="site">

  <header class="hero">
    <div class="hero__photo" role="img" aria-label="Beachfront street with palm trees and houses under a teal tint"></div>
    <div class="brand"><span class="brand__dot"></span>Pinecrest 71 Studios</div>
    <nav class="nav">
      <span>Who we are</span>
      <span class="nav__item--active">What we do</span>
      <span>Visual effects</span>
      <span>Contact</span>
    </nav>
    <h1 class="hero__title">California based visual effects<br>(VFX) company.</h1>
    <p class="hero__lede">Visual effects are often integral to a movie's story and appeal. Although most visual effects work is completed during post-production, it usually must be carefully planned.</p>
    <div class="hero__more">read more.</div>
    <svg class="hero__arrow" width="32" height="32" viewBox="0 0 32 32" aria-hidden="true">
      <circle cx="16" cy="16" r="14" fill="none" stroke="#fff" stroke-width="2"/>
      <path d="M16 9v13M10 16l6 6 6-6" fill="none" stroke="#fff" stroke-width="2"/>
    </svg>
  </header>

  <section class="bio">
    <div class="bio__photo bio__photo--left" role="img" aria-label="Portrait of the studio founder"></div>
    <div class="bio__photo bio__photo--right" role="img" aria-label="Portrait of a team member"></div>
    <h2 class="bio__name">Dale Everett Morrow</h2>
    <p class="bio__intro">Patrick Morrow grew up in Los Angeles and by the young age of 17 was working in the film.</p>
    <span class="bio__cta">click here to read full bio.</span>
    <span class="bio__hint">hover to see more information</span>
  </section>

  <aside class="about-card">
    <h3 class="about-card__title">about</h3>
    <p class="about-card__text">Dale Everett Morrow grew up in Los Angeles and by the young age of 17 was working in the film industry as an on-set Production Assistant on 'The Lighthouse'. By 1999, he began his long journey in to visual effects as a visual effects coordinator at Tidewater Pixel. As the Senior Manager of Meridian Digital Production, Pat went on to develop several artist management teams as Tidewater Pixel expanded globally. He acted as the main connection between Los Angeles and offices in Vancouver, Mumbai, Hyderabad, Malaysia and Taiwan focusing on artist growth and maintaining world class facilities. With on-set, visual effects and with international start ups knowledge, Pat has a range of experience that is difficult to find.</p>
  </aside>

  <h2 class="section-title services__title">what we do.</h2>

  <div class="service" style="top:1333px">
    <div class="service__icon"><svg width="30" height="30" viewBox="0 0 30 30" aria-hidden="true"><path d="M5 24V16M11 24V11M17 24V14M23 24V7" stroke="#e47a22" stroke-width="3"/></svg></div>
    <div><div class="service__name">Statistics</div><p class="service__text">We are entrepreneurs that have founded or co-founded numerous businesses</p></div>
  </div>
  <div class="service" style="top:1430px">
    <div class="service__icon"><svg width="30" height="30" viewBox="0 0 30 30" aria-hidden="true"><path d="M4 23l8-8 5 5 9-11" fill="none" stroke="#e47a22" stroke-width="3"/></svg></div>
    <div><div class="service__name">Pageranking</div><p class="service__text">We are entrepreneurs that have founded or co-founded numerous businesses</p></div>
  </div>
  <div class="service" style="top:1527px">
    <div class="service__icon"><svg width="30" height="30" viewBox="0 0 30 30" aria-hidden="true"><circle cx="15" cy="15" r="10" fill="none" stroke="#e47a22" stroke-width="3"/><circle cx="15" cy="15" r="3" fill="#e47a22"/></svg></div>
    <div><div class="service__name">Education</div><p class="service__text">We are entrepreneurs that have founded or co-founded numerous businesses</p></div>
  </div>

  <p class="services__lead">Visual effects primarily executed in Post-Production, with the use of multiple tools and technologies such as graphic design.</p>
  <div class="services__photo" role="img" aria-label="Modern glass office building against a blue sky"></div>

  <h2 class="section-title about__title">about.</h2>
  <p class="about__text">Formed in 2014, <span class="about__brand">Pinecrest 71 Studios</span> is a visual effects studio based in Marina Vista, CA. Taking their name from early Californian history, Pinecrest 71 Studios looks to continue the <span class="about__accent">Golden State's tradition of strong and reliable visual effects.</span> With close to 20 years in the vfx community, Pinecrest 71 Studios has the ability to service feature films, television, and commercials. Pinecrest 71's capabilities are focused on compositing, 2.5D effects and environments, rotoscope, paint fixes, color timing and other 2D tasks. With a network of talented acquaintances built over the years, <span class="about__brand">Pinecrest 71 Studios</span> can adapt to the clients needs. At a time when budgets and schedules are shrinking Pinecrest 71 Studios' goal is supplying world class visual effects work on a workable budget.</p>

  <section class="location" role="img" aria-label="Map of the studio's area in Southern California">
    <p class="location__text">Lorem ipsum dolor sit amet, consectetur adipiscing elit. Fusce felis ipsum sollicitudin in congue ut, tempus vitae tellus. Ut ornare congue erat.</p>
  </section>

  <footer class="footer">
    <div class="social">
      <span class="social__item"></span>
      <span class="social__item"></span>
      <span class="social__item"></span>
      <span class="social__item social__item--red"></span>
    </div>
    <p class="footer__legal">© 2014 by <b>Pinecrest 71 Studios</b>, LLC. All rights reserved</p>
  </footer>

</div>
</body>
</html>
```